Quiet Motion Honor Project posters to attract attention at trade shows

Our company, LumaFlow, trains and certifies Tai Chi teachers. We have a project called "Quiet Motion Honor Project" and we are working with our government to provide free Tai Chi classes to military veterans. Part of what we are doing is recruiting new instructors to take our training and start teaching our Vets.<br/><br/>We will be attending Fitness conferences throughout the US during 2020 - and we have one coming up next week. I need 3 table posters 18 x 24 to catch the eye of people walking by our booth. <br/><br/>The posters should use images of Tai Chi classes, or images of Veterans or both. I was thinking one poster should attract people by saying something like: "You could make a difference in the life of a Veteran" or "Be a hero to a Hero - teaching Tai Chi to our nation's Veterans" or something like that.<br/><br/>Then I'd like a second poster to take a different approach - something like: Make $100/hour to start! Take your fitness career to the next level with a Tai Chi certification (the highest compensation in the Fitness industry). LumaFlow is recruiting instructors for your area NOW.<br/><br/>The third poster I need is one that Invites conference attendees to try a sample class. I've uploaded a sample poster in the files to give you a rough idea. I made this myself just for basic content example - but I want a much different creative vibe. Hope all this makes sense - please message me if you have questions.

Target Market(s)

Fitness conference attendees - fitness trainers, yoga teachers

Industry/Entity Type

Fitness

Font styles to use
Sans Serif

Colors

Designer to choose colors to be used in the design.

Requirements
Must have
• our logo, images of Veterans, images of fitness trainers/yoga teachers or both.Clear copy and call to action

```html
<!DOCTYPE html>
<html lang="en">
<head>
<meta charset="utf-8">
<title>Quiet Motion Honor Project – Sample Class Poster</title>
<link href="https://fonts.googleapis.com/css2?family=Saira+Stencil+One&family=Archivo:wght@800&display=swap" rel="stylesheet">
<style>
  :root {
    --page: #ffffff;
    --navy: #102c3b;
    --navy-light: #2b4a5a;
    --gold: #f6a800;
    --white: #ffffff;
  }
  html, body {
    margin: 0;
    width: 1200px;
    height: 900px;
    overflow: hidden;
    background: var(--page);
  }
  .canvas {
    position: relative;
    width: 1200px;
    height: 900px;
  }
  .poster {
    position: absolute;
    left: 310px;
    top: 27px;
    width: 578px;
    height: 846px;
    background: var(--navy);
  }
  .poster-edge {
    position: absolute;
    left: 300px;
    top: 20px;
    width: 598px;
    height: 860px;
  }
  .hero-figure {
    position: absolute;
    left: 95px;
    top: 18px;
    width: 400px;
    height: 460px;
    background: radial-gradient(ellipse at 50% 40%, var(--navy-light) 0%, var(--navy) 70%);
  }
  .date-ribbon {
    position: absolute;
    left: 802px;
    top: 0;
    width: 100px;
    height: 168px;
  }
  .ribbon-text {
    position: absolute;
    left: 802px;
    top: 34px;
    width: 100px;
    text-align: center;
    font-family: "Archivo", sans-serif;
    font-weight: 800;
    color: var(--navy);
    line-height: 1.05;
  }
  .ribbon-day { font-size: 22px; }
  .ribbon-time { font-size: 30px; }
  .headline {
    position: absolute;
    left: 0;
    top: 300px;
    width: 578px;
    margin: 0;
    text-align: center;
    font-family: "Saira Stencil One", sans-serif;
    font-weight: 400;
    color: var(--gold);
    -webkit-text-stroke: 8px var(--white);
    paint-order: stroke fill;
    line-height: 0.98;
    letter-spacing: 2px;
  }
  .headline span { display: block; }
  .headline .line-sm { font-size: 74px; }
  .headline .line-lg { font-size: 100px; }
  .copy {
    position: absolute;
    margin: 0;
    font-family: "Archivo", sans-serif;
    font-weight: 800;
    font-size: 21px;
    line-height: 1.2;
    color: var(--white);
    text-transform: uppercase;
  }
  .copy em { font-style: normal; color: var(--gold); }
  .copy-program { left: 53px; top: 620px; width: 460px; }
  .copy-invite { right: 48px; top: 753px; width: 470px; text-align: right; }
</style>
</head>
<body>
<div class="canvas">
  <svg class="poster-edge" viewBox="0 0 598 860" aria-hidden="true">
    <polygon fill="#102c3b" points="10,8 40,4 90,9 160,5 240,8 320,4 400,9 480,5 560,8 592,4 596,60 590,140 595,220 589,320 594,420 590,520 596,620 590,720 595,800 592,852 520,856 440,851 360,856 280,852 200,856 120,851 40,856 6,852 10,780 4,680 9,580 4,480 9,380 5,280 9,180 4,80"/>
  </svg>
  <main class="poster">
    <div class="hero-figure" role="img" aria-label="Line illustration of a person in a flowing robe performing a tai chi stance"></div>
    <h1 class="headline">
      <span class="line-sm">QUIET MOTION</span>
      <span class="line-lg">HONOR</span>
      <span class="line-lg">PROJECT</span>
    </h1>
    <p class="copy copy-program">A new <em>program</em> from the <em>federal goverment</em> pays you to offer free <em>tai chi</em> to our <em>nation’s heros</em></p>
    <p class="copy copy-invite">Try <em>LumaFlow</em> Flow - the tai chi class approved for vets - <em>here at Harbor Expo</em></p>
  </main>
  <svg class="date-ribbon" viewBox="0 0 100 168" aria-hidden="true">
    <polygon fill="#f6a800" points="0,0 100,0 100,168 50,135 0,168"/>
    <polygon fill="#102c3b" points="50,6 53.5,15 63,15 55.5,20.5 58.5,30 50,24 41.5,30 44.5,20.5 37,15 46.5,15"/>
  </svg>
  <div class="ribbon-text">
    <div class="ribbon-day">FRIDAY</div>
    <div class="ribbon-time">6 PM</div>
  </div>
</div>
</body>
</html>
```